3 pages of UI design for AdTech Startup

We need 3 pages of UI design for a new AdTech company located in Seattle called KESTREL Systems.

We put digital, mobile billboards on college campuses throughout the country. This design project involves our back-end customer dashboard.

Page 1- Dashboard home page
page 2- Manage ads screen (see File 3 below for the screenshot of our current design). Please match the design of all 3 screens so there is consistency
page 3-Detailed Zone screen (see file 16 below). This page looks similar to the first page but gives a more detailed overview and a larger map.

The features and functionality are already built but we are lacking an aesthetically pleasing and slick design. Looking for someone who can match our website look to this new dashboard space. Our company reflects modern, clean, elegant design that is straight-forward and user friendly (main inspiration is VOLTA, we love their design and feel).

Target Market(s)

-Local business owner, marketing directors, and national advertising and marketing agencies

Industry/Entity Type

Advertising

Number of Pages Required

3 page

Font styles to use
Other font styles liked:
• Proxima Nova- Thin for body text, Light for title

Colors
85cae6
33a6d7
0292cd
ffffff

Requirements
Nice to have
• Please include enough detail so that my developer can look at the design you come up with and translate it to html. Please include spacing, fonts, color numbers. My developer is going to look at your creation and recreate it in html format

```html
<!DOCTYPE html>
<html lang="en">
<head>
<meta charset="utf-8">
<title>KESTREL Insights Summary</title>
<link href="https://fonts.googleapis.com/css2?family=Montserrat:wght@200;300;400;500&display=swap" rel="stylesheet">
<style>
:root{
  --sidebar:#2e2e30;
  --header:#58595d;
  --header-dark:#3e3f42;
  --tab-active:#c3c4c6;
  --tab-text:#d8d9db;
  --sky-top:#9fd4ea;
  --sky-mid:#33a6d7;
  --sky-bottom:#1c88c2;
  --panel:rgba(98,122,138,.78);
  --card:rgba(70,112,138,.85);
  --card-strip:#303033;
  --map-dark:#2b3a34;
  --map-mid:#3c4a3a;
  --white:#ffffff;
  --accent:#33a6d7;
  --grid:rgba(255,255,255,.55);
  --footer:#5b5c60;
}
*{margin:0;padding:0;box-sizing:border-box}
html,body{width:960px;height:1200px;overflow:hidden}
body{position:relative;font-family:"Montserrat",sans-serif;color:var(--white);background:var(--sidebar)}
.sidebar{position:absolute;left:0;top:0;width:42px;height:1200px;background:var(--sidebar)}
.topbar{position:absolute;left:0;top:0;width:960px;height:42px;background:var(--header)}
.brand-square{position:absolute;left:13px;top:14px;width:14px;height:14px;background:var(--accent)}
.brand-name{position:absolute;left:48px;top:8px;font-weight:200;font-size:23px;line-height:26px;letter-spacing:.5px;color:var(--white);white-space:nowrap}
.page-title{position:absolute;left:166px;top:19px;font-weight:300;font-size:13px;white-space:nowrap}
.date-range{position:absolute;left:300px;top:22px;font-weight:400;font-size:10px;letter-spacing:2px;white-space:nowrap}
.search{position:absolute;left:767px;top:13px;width:20px;height:20px;background:#6c6d71}
.search svg{position:absolute;left:4px;top:4px}
.user{position:absolute;left:795px;top:0;width:113px;height:42px;background:var(--header-dark)}
.avatar{position:absolute;left:10px;top:12px;width:17px;height:17px;border-radius:50%;background:#8a8c90}
.badge{position:absolute;left:21px;top:9px;width:8px;height:8px;border-radius:50%;background:var(--accent)}
.user-name{position:absolute;left:34px;top:16px;font-size:7.5px;font-weight:300;color:#b8b9bc;white-space:nowrap}
.user-caret{position:absolute;left:100px;top:19px}
.client{position:absolute;right:6px;top:14px;font-size:12px;font-weight:500;letter-spacing:.3px;white-space:nowrap}
.tabs{position:absolute;left:42px;top:42px;height:24px;display:flex;background:var(--header)}
.tab{width:82px;height:24px;line-height:24px;text-align:center;font-size:11.5px;font-weight:300;color:var(--tab-text)}
.tab.is-active{background:var(--tab-active);color:#6e6f73}
.tab.is-active::after{content:"";display:inline-block;margin-left:6px;border:3px solid transparent;border-bottom:4px solid #6e6f73;vertical-align:3px}
.main{position:absolute;left:42px;top:42px;width:918px;height:1118px;background:linear-gradient(180deg,var(--sky-top) 0%,var(--sky-mid) 42%,var(--sky-bottom) 100%);z-index:-1}
.chart{position:absolute;left:0;top:0}
.stats{position:absolute;background:var(--panel)}
.stat{position:absolute;left:17px}
.stat dt{font-size:7.5px;letter-spacing:2.6px;font-weight:400}
.stat dd{margin-top:5px;font-size:11.5px;letter-spacing:2.8px;font-weight:400;white-space:nowrap}
.stats--chart{left:799px;top:96px;width:161px;height:282px;box-shadow:0 2px 4px rgba(0,0,0,.25)}
.zone{position:absolute;left:84px;width:876px;height:282px;background:var(--card);box-shadow:0 2px 4px rgba(0,0,0,.25)}
.zone--one{top:486px}
.zone--two{top:802px}
.zone-strip{position:absolute;left:0;top:0;width:38px;height:282px;background:var(--card-strip)}
.zone-map{position:absolute;left:38px;top:23px;width:656px;height:236px;background:linear-gradient(100deg,#4d5750 0%,var(--map-dark) 30%,var(--map-mid) 60%,#2f4530 100%)}
.zone .stats{left:715px;top:0;width:161px;height:282px;background:none}
.s1{top:24px}.s2{top:90px}.s3{top:162px}.s4{top:234px}
.footer{position:absolute;left:42px;top:1160px;width:918px;height:40px;background:var(--footer);padding:8px 0 0 40px;font-size:7.5px;line-height:15px;font-weight:400}
</style>
</head>
<body>
<div class="sidebar"></div>
<div class="main"></div>

<header class="topbar">
  <span class="brand-square" aria-hidden="true"></span>
  <span class="brand-name">KESTREL</span>
  <span class="page-title">Insights Summary</span>
  <span class="date-range">2016/01/01 - 2016/06/15</span>
  <div class="search"><svg width="12" height="12" viewBox="0 0 12 12" aria-hidden="true"><circle cx="5" cy="5" r="3.6" fill="none" stroke="#a9aaad" stroke-width="1.4"/><path d="M7.6 7.6 L11 11" stroke="#a9aaad" stroke-width="1.6"/></svg></div>
  <div class="user">
    <span class="avatar"></span><span class="badge"></span>
    <span class="user-name">Dana Whitfield</span>
    <svg class="user-caret" width="6" height="4" viewBox="0 0 6 4" aria-hidden="true"><path d="M0 0 H6 L3 4Z" fill="#b8b9bc"/></svg>
  </div>
  <span class="client">ARENA</span>
</header>

<nav class="tabs">
  <span class="tab">Yearly</span>
  <span class="tab is-active">Monthly</span>
  <span class="tab">Daily</span>
</nav>

<svg class="chart" width="800" height="460" viewBox="0 0 800 460" role="img" aria-label="Monthly impressions line chart">
  <g stroke="var(--grid)" stroke-width="1" stroke-dasharray="2 3">
    <line x1="124" y1="122" x2="776" y2="122"/><line x1="124" y1="165" x2="776" y2="165"/>
    <line x1="124" y1="207" x2="776" y2="207"/><line x1="124" y1="249" x2="776" y2="249"/>
    <line x1="124" y1="291" x2="776" y2="291"/><line x1="124" y1="334" x2="776" y2="334"/>
    <line x1="216" y1="95" x2="216" y2="376"/><line x1="309" y1="95" x2="309" y2="376"/>
    <line x1="402" y1="95" x2="402" y2="376"/><line x1="495" y1="95" x2="495" y2="376"/>
    <line x1="589" y1="95" x2="589" y2="376"/><line x1="682" y1="95" x2="682" y2="376"/>
  </g>
  <g stroke="rgba(255,255,255,.6)" stroke-width="1">
    <line x1="169" y1="249" x2="169" y2="376"/><line x1="730" y1="292" x2="730" y2="376"/>
  </g>
  <path d="M124 370 V376 H776 V370" fill="none" stroke="rgba(255,255,255,.75)" stroke-width="1.2"/>
  <g stroke="rgba(255,255,255,.75)"><line x1="216" y1="376" x2="216" y2="381"/><line x1="309" y1="376" x2="309" y2="381"/><line x1="402" y1="376" x2="402" y2="381"/><line x1="495" y1="376" x2="495" y2="381"/><line x1="589" y1="376" x2="589" y2="381"/><line x1="682" y1="376" x2="682" y2="381"/></g>
  <polyline points="169,249 216,165 308,207 402,122 496,249 589,206 682,185 730,292" fill="none" stroke="#ffffff" stroke-width="1.8"/>
  <g fill="#2d3b48" stroke="#ffffff" stroke-width="2">
    <circle cx="169" cy="249" r="6"/><circle cx="216" cy="165" r="6"/><circle cx="308" cy="207" r="6"/>
    <circle cx="402" cy="122" r="6"/><circle cx="496" cy="249" r="6"/><circle cx="589" cy="206" r="6"/>
    <circle cx="682" cy="185" r="6"/><circle cx="730" cy="292" r="6" fill="#4a7a96"/>
  </g>
  <g fill="rgba(255,255,255,.85)" font-family="Montserrat, sans-serif" font-weight="300" font-size="15" text-anchor="end">
    <text x="106" y="127">90</text><text x="106" y="212">60</text><text x="106" y="297">30</text>
  </g>
  <g fill="rgba(255,255,255,.85)" font-family="Montserrat, sans-serif" font-weight="300" font-size="11" text-anchor="middle">
    <text x="169" y="403">JAN</text><text x="262" y="403">FEB</text><text x="357" y="403">MAR</text>
    <text x="449" y="403">APR</text><text x="543" y="403">MAY</text><text x="636" y="403">JUN</text><text x="730" y="403">JUL</text>
  </g>
  <ellipse cx="486" cy="444" rx="340" ry="1.6" fill="rgba(20,50,70,.55)"/>
</svg>

<dl class="stats stats--chart">
  <div class="stat s1"><dt>ROTATIONS</dt><dd>85</dd></div>
  <div class="stat s2"><dt>TIME</dt><dd>21.25 min</dd></div>
  <div class="stat s3"><dt>IMPRESSIONS</dt><dd>595</dd></div>
  <div class="stat s4"><dt>MILES</dt><dd>0.3 miles</dd></div>
</dl>

<section class="zone zone--one">
  <div class="zone-strip"></div>
  <div class="zone-map" role="img" aria-label="Satellite map of the campus zone route"></div>
  <dl class="stats">
    <div class="stat s1"><dt>ROTATIONS</dt><dd>85</dd></div>
    <div class="stat s2"><dt>TIME</dt><dd>21.25 min</dd></div>
    <div class="stat s3"><dt>IMPRESSIONS</dt><dd>595</dd></div>
    <div class="stat s4"><dt>MILES</dt><dd>0.3 miles</dd></div>
  </dl>
</section>

<section class="zone zone--two">
  <div class="zone-strip"></div>
  <div class="zone-map" role="img" aria-label="Satellite map of the campus zone route"></div>
  <dl class="stats">
    <div class="stat s1"><dt>ROTATIONS</dt><dd>85</dd></div>
    <div class="stat s2"><dt>TIME</dt><dd>21.25 min</dd></div>
    <div class="stat s3"><dt>IMPRESSIONS</dt><dd>595</dd></div>
    <div class="stat s4"><dt>MILES</dt><dd>0.3 miles</dd></div>
  </dl>
</section>

<footer class="footer">
  <div>Home | About | Products | Services | Contact</div>
  <div>Privacy Policy | Terms of use</div>
</footer>
</body>
</html>
```